Brontaro Web Site

Redesigned web site for Brontaro Ltd (www.brontaro-example.co.uk). This is to feature new logo (attached). Brontaro Ltd is a company which specialises in Geographic Information Systems and Geographic data - we call ourselves GIS Data Specialists. We are looking for something which conveys our professionalism and our experience. There will be more pages than on the current Brontaro website. There will be: Home, Data Migration, Data Cleansing & Validation, Data Analysis, Data Maintenance, Data Quality and an About Us page. All these should be accessible from each page on the website.
Updates
I didn't really think to say that the content of the web site is going to change from the current one we have. There will be more pages than on the current one. They will be: Home, Data Migration, Data Cleansing & Validation, Data Analysis, Data Maintenance, Data Quality and an About Us page. All these should be accessible from each page on the website. I didn't really think through the fact that the number of pages / areas to access can influence the layout of the site, sorry.
Target Market(s)
Utility Companies (e.g. telecommunications providers, energy companies), local government.
Industry/Entity Type
It Company
Look and feel

```html
<!DOCTYPE html>
<html lang="en">
<head>
<meta charset="utf-8">
<title>Brontaro – Software Development</title>
<link rel="stylesheet" href="https://fonts.googleapis.com/css2?family=Arimo:wght@400;700&family=Roboto:wght@300;400&display=swap">
<style>
  :root {
    --page-bg: #ffffff;
    --brand-grey: #555a5e;
    --brand-teal: #5aa9a0;
    --tab-top: #a9a9a9;
    --tab-bottom: #7d7d7d;
    --tab-active-top: #e01414;
    --tab-active-bottom: #b30000;
    --hero-blue: #3e80b6;
    --hero-edge: #2e6e9f;
    --subnav-blue: #1a689e;
    --strip-blue: #4288bd;
    --body-text: #4a4a4a;
    --frame-line: #c8c8c8;
    --footer-top: #5d5d5d;
    --footer-bottom: #7c7c7c;
    --footer-head: #c9c9c9;
    --footer-link: #b5b5b5;
    --social-navy: #1d5f8a;
    --social-blue: #3a63a8;
    --social-sky: #4fb3dc;
    --social-orange: #e8802c;
  }
  * { box-sizing: border-box; margin: 0; padding: 0; }
  html, body { width: 1200px; height: 1190px; overflow: hidden; background: var(--page-bg); }
  .canvas { position: relative; width: 1200px; height: 1190px; overflow: hidden; font-family: "Arimo", Arial, sans-serif; }

  .brand { position: absolute; left: 60px; top: 8px; height: 126px; }
  .brand-mark { position: absolute; left: 4px; top: 34px; width: 58px; height: 58px; border-radius: 50%; background: var(--brand-teal); }
  .brand-name { position: absolute; left: 79px; top: 38px; font-size: 52px; font-weight: 700; color: var(--brand-grey); letter-spacing: -1px; white-space: nowrap; line-height: 1; }
  .brand-tagline { position: absolute; left: 81px; top: 91px; font-size: 22px; font-weight: 400; color: var(--brand-grey); white-space: nowrap; line-height: 1; }

  .main-nav { position: absolute; left: 0; top: 133px; width: 1200px; height: 35px; }
  .main-nav a { position: absolute; top: 0; height: 33px; line-height: 35px; text-align: center; color: #fff; font-weight: 700; font-size: 15.5px; text-decoration: none; border-radius: 6px 6px 0 0; background: linear-gradient(var(--tab-top), var(--tab-bottom)); white-space: nowrap; overflow: hidden; }
  .main-nav a.is-active { background: linear-gradient(var(--tab-active-top), var(--tab-active-bottom)); }
  .main-nav a.is-tight { font-size: 15px; letter-spacing: -0.2px; }
  .main-nav::after { content: ""; position: absolute; left: 0; top: 33px; width: 1200px; height: 2px; background: var(--hero-edge); }

  .hero { position: absolute; left: 0; top: 168px; width: 1200px; height: 240px; background: var(--hero-blue); border-bottom: 2px solid #2a6290; }
  .hero-title { position: absolute; left: 139px; top: 44px; font-size: 37px; font-weight: 700; line-height: 44px; color: #fff; text-shadow: 2px 3px 5px rgba(0,0,0,0.45); }
  .hero-intro { position: absolute; left: 139px; top: 137px; font-family: "Roboto", Arial, sans-serif; font-size: 22px; line-height: 38px; color: #fff; }
  .hero-visual { position: absolute; left: 755px; top: 12px; width: 240px; height: 235px; border-radius: 4px; background: linear-gradient(135deg, #f4f4f4 0%, #dfe6ec 45%, #3a8a6a 75%, #c94b3a 100%); }

  .sub-nav { position: absolute; left: 0; top: 408px; width: 1200px; height: 38px; background: var(--subnav-blue); color: #fff; font-size: 16px; font-weight: 700; line-height: 38px; padding-left: 139px; white-space: nowrap; }
  .sub-nav .divider { margin: 0 11px; }
  .sub-strip { position: absolute; left: 0; top: 446px; width: 1200px; height: 8px; background: var(--strip-blue); }

  .content-title { position: absolute; left: 132px; top: 478px; font-size: 35px; font-weight: 700; color: var(--brand-teal); line-height: 1.1; white-space: nowrap; }
  .content-body { position: absolute; left: 133px; top: 523px; width: 565px; font-family: "Roboto", Arial, sans-serif; font-weight: 300; font-size: 14.2px; line-height: 22.6px; color: var(--body-text); }
  .content-body p { margin-bottom: 8px; }

  .content-figure { position: absolute; left: 732px; top: 493px; width: 356px; height: 247px; border: 1px solid var(--frame-line); padding: 5px; background: #fff; }
  .content-figure div { width: 100%; height: 100%; background: linear-gradient(120deg, #d9d9d9 0%, #8e8e8e 40%, #6a5bc8 65%, #d9a0d0 85%, #e9e9e9 100%); }

  .site-footer { position: absolute; left: 0; top: 1062px; width: 1200px; height: 128px; background: linear-gradient(var(--footer-top), var(--footer-bottom)); font-size: 13.5px; line-height: 17.5px; }
  .footer-col { position: absolute; top: 18px; }
  .footer-col h4 { font-size: 13.5px; font-weight: 700; color: var(--footer-head); }
  .footer-col span { display: block; color: var(--footer-link); }
  .footer-legal { position: absolute; left: 696px; top: 18px; font-weight: 700; color: var(--footer-head); white-space: nowrap; }
  .social { position: absolute; top: 46px; width: 27px; height: 27px; border-radius: 4px; }
</style>
</head>
<body>
<div class="canvas">
  <header class="brand">
    <span class="brand-mark"></span>
    <span class="brand-name">Brontaro</span>
    <span class="brand-tagline">GIS Data Specialists</span>
  </header>

  <nav class="main-nav">
    <a class="is-active" style="left:144px;width:77px">Home</a>
    <a style="left:224px;width:137px">Data Migration</a>
    <a class="is-tight" style="left:366px;width:224px">Data Cleansing &amp; Validation</a>
    <a style="left:594px;width:134px">Data Analysis</a>
    <a class="is-tight" style="left:732px;width:140px">Data Maintenance</a>
    <a style="left:876px;width:137px">Data Quality</a>
    <a style="left:1017px;width:110px">About Us</a>
  </nav>

  <section class="hero">
    <h1 class="hero-title">Experienced GIS Data<br>Specialists working for you.</h1>
    <p class="hero-intro">Aliquipit nis nis ad eriuscil utem vent prationsed el<br>digna alit nonulluptat, venibh exerostie magnaeril ius.</p>
    <div class="hero-visual" role="img" aria-label="Software box with a glossy disc beside it"></div>
  </section>

  <nav class="sub-nav">Data Consultancy<span class="divider">|</span>System Consultancy<span class="divider">|</span>Software Development</nav>
  <div class="sub-strip"></div>

  <h2 class="content-title">Software Development</h2>
  <div class="content-body">
    <p>At Brontaro, we make it our business to understand our client's needs, their core business and strategic requirements and then provide carefully customised software to ensure these requirements are met. To achieve this we apply modern software construction techniques and follow industry best practices to produce software of the highest quality.</p>
    <p>Our software development team consists of skilled analysts, designers and programmers who are trained in the latest technologies and have real world experience through the development of both 'off the shelf' applications and bespoke customer solutions.</p>
    <p>Brontaro are platform independent and have established development partnerships with many of the world's leading GIS product vendors such as Gridline Network Systems, Mapvale, Draftmere, Terrasyn and Kestrand. These partnerships enhance our ability to react to non-standard requests and, through us, provide our clients access to the GIS vendor knowledge base.</p>
    <p>Our team is therefore well versed in all leading GIS software data formats and industry standard mark-up languages. Our own toolbox of data migration utilities and in-house translators assist us in the data cleansing, normalisation and migration process thus minimising solution delivery timescales.</p>
  </div>
  <figure class="content-figure"><div role="img" aria-label="Stack of disc cases with a shiny disc in front"></div></figure>

  <footer class="site-footer">
    <div class="footer-col" style="left:180px"><h4>The Service</h4><span>About</span><span>Browse</span><span>Log In</span></div>
    <div class="footer-col" style="left:342px"><h4>Support</h4><span>Contact Us</span><span>FAQ</span></div>
    <div class="footer-col" style="left:495px"><h4>Legal</h4><span>Privacy Policy</span><span>Terms &amp; Conditions</span></div>
    <div class="footer-legal">© 2010 Brontaro Ltd. Registered in Scotland No. 482731</div>
    <span class="social" style="left:909px;background:var(--social-navy)" role="img" aria-label="Professional network link"></span>
    <span class="social" style="left:949px;background:var(--social-blue)" role="img" aria-label="Social network link"></span>
    <span class="social" style="left:989px;background:var(--social-sky)" role="img" aria-label="Microblog link"></span>
    <span class="social" style="left:1029px;background:var(--social-orange)" role="img" aria-label="News feed link"></span>
  </footer>
</div>
</body>
</html>
```